Law Firm Website, easily updated by User

We are a regional Labor and Employment Law Firm with a tired outdated website. We are looking for a clean easy to use website that will allow us to easily update information and articles in house. Our current website can be found at www.quillbrookcounsel.com

Industry/Entity Type

Labor

Number of Pages Required

5+ page

Colors
0655a3

Requirements
Must have
• Content easily updated by user
Nice to have
• crisp clean pages
Should not have
• stock pictures

```html
<!DOCTYPE html>
<html lang="en">
<head>
<meta charset="utf-8">
<title>Quillbrook &amp; Associates, P.C.</title>
<link href="https://fonts.googleapis.com/css2?family=Roboto:wght@300;400;500;700&family=Roboto+Condensed:wght@300;400&display=swap" rel="stylesheet">
<style>
:root{
  --blue:#0655a3;
  --blue-dark:#0a3f7a;
  --ink:#1f1f1f;
  --dark:#2a2828;
  --grey:#5a5858;
  --text:#555;
  --white:#fff;
}
*{box-sizing:border-box;margin:0;padding:0}
html,body{width:1200px;height:3066px;overflow:hidden}
body{font-family:"Roboto",sans-serif;color:var(--ink);background:var(--white);position:relative}
section,header,footer{position:absolute;left:0;width:1200px}

/* header */
.site-header{top:0;height:106px;background:var(--white)}
.brand{position:absolute;left:268px;top:14px;display:flex;align-items:center;gap:8px}
.brand-square{width:34px;height:34px;background:var(--blue)}
.brand-text{display:flex;flex-direction:column}
.brand-name{font-size:18px;font-weight:500;color:var(--blue-dark);line-height:22px;white-space:nowrap;border-bottom:2px solid var(--blue);padding-bottom:1px}
.brand-tagline{font-size:6.5px;font-weight:500;color:var(--blue-dark);letter-spacing:.2px;margin-top:2px;white-space:nowrap}
.header-contacts{position:absolute;right:268px;top:30px;display:flex;gap:16px;font-size:9px;color:var(--text);align-items:center;white-space:nowrap}
.header-contacts span{display:flex;align-items:center;gap:6px}
.header-rule{position:absolute;left:268px;right:268px;top:74px;height:1px;background:#ddd}
.main-nav{position:absolute;left:268px;top:84px;display:flex;gap:22px;font-size:11px;color:#333}
.main-nav a{color:inherit;text-decoration:none;padding-bottom:6px}
.main-nav a.active{border-bottom:2px solid var(--blue)}
.search-icon{position:absolute;right:268px;top:80px}

/* hero */
.hero{top:106px;height:368px;background:linear-gradient(100deg,#0b3f84 0%,#1762b4 45%,#a9b8cb 75%,#d8dde4 100%)}
.hero-caption{position:absolute;left:270px;top:140px;color:var(--white)}
.hero-caption .kicker{font-size:19px;font-weight:500;letter-spacing:.5px}
.hero-caption .headline{font-family:"Roboto Condensed",sans-serif;font-weight:300;font-size:32px;line-height:34px;margin-top:6px}
.hero-arrow{position:absolute;top:160px}

/* welcome */
.welcome{top:474px;height:252px;text-align:center}
.welcome h1{font-size:19px;font-weight:700;width:260px;margin:38px auto 20px;line-height:26px}
.welcome p{font-size:8.5px;color:var(--text);width:660px;margin:0 auto 12px;line-height:13px}

/* tagline band */
.tagline-band{top:767px;height:183px;background:linear-gradient(180deg,#2b2b2b,#3d3b3b)}
.tagline-band p{position:absolute;top:70px;width:100%;text-align:center;color:var(--white);font-size:12px;font-weight:500}
.section-cap{top:905px;height:76px}
.section-cap h2{position:absolute;top:30px;width:100%;text-align:center;font-size:21px;font-weight:700;color:var(--ink)}

/* attorneys */
.attorneys{top:981px;height:362px}
.attorney-list{position:absolute;left:270px;top:35px;display:flex;gap:22px}
.attorney{width:206px;text-align:center}
.attorney .portrait{width:206px;height:220px;border:6px solid var(--white);box-shadow:0 4px 10px rgba(0,0,0,.35)}
.attorney .name{margin-top:18px;font-size:14px;font-weight:300;color:#333}
.attorney .role{font-size:9px;letter-spacing:2px;color:var(--blue);font-weight:700;margin-top:2px}

/* practice */
.practice{top:1343px;height:574px;background:linear-gradient(90deg,#3a3838,#555352 50%,#3a3838)}
.practice h2{position:absolute;top:70px;width:100%;text-align:center;color:var(--white);font-size:22px;font-weight:700}
.practice-cols{position:absolute;top:160px;left:0;width:1200px;display:grid;grid-template-columns:600px 600px}
.col-left{display:flex;flex-direction:column;align-items:flex-end}
.col-right{display:flex;flex-direction:column;align-items:flex-start;padding-left:1px}
.col-head{font-size:18px;color:var(--white);font-weight:400;height:46px;padding:0 10px}
.col-left .col-head{padding-right:16px}
.item{height:22px;margin-bottom:6px;font-size:11.5px;color:var(--white);display:flex;align-items:center;gap:10px;padding:0 12px}
.col-left .item{background:var(--blue)}
.col-right .item{background:var(--grey)}
.star{font-size:12px}

/* chat */
.chat{top:1917px;height:266px;text-align:center}
.chat .mark{position:absolute;left:584px;top:74px;width:32px;height:40px;background:var(--blue-dark)}
.chat p{position:absolute;top:160px;width:100%;font-size:20px;font-weight:300;color:#333}

/* form */
.evaluation{top:2183px;height:256px;background:var(--dark)}
.evaluation h2{position:absolute;top:30px;width:100%;text-align:center;color:var(--white);font-size:19px;font-weight:700}
.evaluation .sub{position:absolute;top:56px;width:100%;text-align:center;color:#ddd;font-size:11px}
.field{position:absolute;top:92px;height:30px;width:153px;background:#e4e4e4;font-size:9px;color:#555;padding:10px 8px}
.field.message{top:139px;left:268px;width:490px;height:80px}
.send{position:absolute;left:775px;top:139px;width:153px;height:80px;background:var(--blue);color:var(--white);font-size:13px;font-weight:500;display:flex;align-items:center;justify-content:center}

/* contact */
.contact{top:2439px;height:535px;background:linear-gradient(180deg,#e9e9e9,#f6f6f6);text-align:center}
.contact .icon{position:absolute;left:578px;top:58px;width:44px;height:50px;background:var(--dark)}
.contact h2{position:absolute;top:138px;width:100%;font-size:20px;font-weight:500}
.contact-lines{position:absolute;top:212px;left:0;width:100%;display:flex;justify-content:center;gap:60px}
.contact-lines .label{font-size:20px;font-weight:300;color:#333}
.contact-lines .value{font-size:20px;font-weight:700;color:var(--ink);margin-top:4px}
.email-box{position:absolute;left:374px;top:294px;width:452px;height:64px;border:2px solid #222;font-size:20px;font-weight:500;display:flex;align-items:center;justify-content:center}
.address{position:absolute;top:380px;width:100%;font-size:9px;color:#333}
.social{position:absolute;top:420px;left:0;width:100%;display:flex;justify-content:center;gap:10px}
.social span{width:44px;height:44px;border-radius:50%;background:var(--blue-dark)}

.site-footer{top:2974px;height:92px;background:var(--white);font-size:9px;color:#333}
.site-footer .copy{position:absolute;left:268px;top:44px}
</style>
</head>
<body>

<header class="site-header">
  <div class="brand">
    <span class="brand-square"></span>
    <div class="brand-text">
      <span class="brand-name">Quillbrook &amp; Associates, P.C.</span>
      <span class="brand-tagline">EMPLOYMENT COUNSELING, LITIGATION, LABOR &amp; BENEFITS LAW</span>
    </div>
  </div>
  <div class="header-contacts">
    <span><svg width="14" height="10" viewBox="0 0 14 10"><rect width="14" height="10" fill="#0655a3"/><path d="M0 0l7 5 7-5" stroke="#fff" fill="none"/></svg>info@quillbrookcounsel.com</span>
    <span><svg width="14" height="12" viewBox="0 0 14 12"><path d="M2 4q5-5 10 0l-2 2-2-1H6L4 6z" fill="#0655a3"/><rect x="3" y="6" width="8" height="5" fill="#0655a3"/></svg>(555) 014 - 2270</span>
    <span><svg width="14" height="12" viewBox="0 0 14 12"><rect x="1" y="4" width="12" height="7" fill="#0655a3"/><rect x="4" y="0" width="6" height="4" fill="#0655a3"/></svg>(555) 014 - 2285</span>
  </div>
  <div class="header-rule"></div>
  <nav class="main-nav">
    <a class="active">Main</a><a>Contact Us</a><a>Attorneys</a><a>Practice Areas</a><a>FAQ</a><a>In The News</a><a>For Employers</a>
  </nav>
  <svg class="search-icon" width="18" height="18" viewBox="0 0 18 18"><circle cx="7" cy="7" r="5.5" stroke="#0655a3" stroke-width="2.5" fill="none"/><path d="M11 11l6 6" stroke="#0655a3" stroke-width="3"/></svg>
</header>

<section class="hero" role="img" aria-label="Two colleagues discussing documents at an office desk">
  <svg class="hero-arrow" style="left:30px" width="22" height="44" viewBox="0 0 22 44"><path d="M20 2L3 22l17 20" stroke="#fff" stroke-width="2" fill="none"/></svg>
  <div class="hero-caption">
    <div class="kicker">COUNSELING AND ADVISING CLIENT</div>
    <div class="headline">EXCLUSIVELY ON LAWS<br>OF THE WORKPLACE</div>
  </div>
  <svg class="hero-arrow" style="right:30px" width="22" height="44" viewBox="0 0 22 44"><path d="M2 2l17 20L2 42" stroke="#fff" stroke-width="2" fill="none"/></svg>
</section>

<section class="welcome">
  <h1>WELCOME TO QUILLBROOK &amp; ASSOCIATES, P.C.</h1>
  <p>QUILLBROOK &amp; ASSOCIATES, P.C. handles only labor, employment and benefits matters. This includes representing employers in state and federal court, before administrative and quasi-judicial agencies, and in negotiations, arbitrations and union organizing campaigns.</p>
  <p>Our attorneys provide a diverse range of counseling and training in areas of the law such as discrimination, sexual harassment, wage and hour issues, Family and Medical Leave Act, HIPPA and reductions-in-force. The attorneys provide hands-on assistance and guidance in the event of government audits, strikes and other daily crises.</p>
  <p>Our broad spectrum of clients includes non-profit agencies and industries including finance, insurance, publishing, transportation, manufacturing, health services, construction, food products and retail stores.</p>
</section>

<svg style="position:absolute;top:726px;left:0" width="1200" height="42" viewBox="0 0 1200 42">
  <polygon points="500,42 540,0 690,0 650,42" fill="#0655a3"/>
  <polygon points="475,42 495,20 505,20 485,42" fill="#0655a3" opacity=".6"/>
  <polygon points="695,20 705,20 685,42 675,42" fill="#0655a3" opacity=".6"/>
</svg>
<section class="tagline-band" role="img" aria-label="Dark background of law books on a shelf">
  <p>COUNSELING AND ADVISING CLIENTS EXCLUSIVELY ON LAWS OF THE WORKPLACE</p>
</section>
<section class="section-cap">
  <svg width="1200" height="76" viewBox="0 0 1200 76" style="position:absolute;top:0;left:0">
    <polygon points="275,0 930,0 930,76 230,76" fill="#fff"/>
    <polygon points="235,45 260,0 280,0 255,45" fill="#bbb"/>
    <polygon points="930,45 955,0 975,0 950,45" fill="#bbb"/>
  </svg>
  <h2>QUILLBROOK &amp; ASSOCIATES ATTORNEYS</h2>
</section>

<section class="attorneys">
  <div class="attorney-list">
    <div class="attorney"><div class="portrait" role="img" aria-label="Portrait of attorney Martin Quillbrook" style="background:linear-gradient(180deg,#6d6a68,#3b3a3c)"></div><div class="name">Martin Quillbrook</div><div class="role">LAW OFFICE</div></div>
    <div class="attorney"><div class="portrait" role="img" aria-label="Portrait of attorney Dana Whitlock at a desk" style="background:linear-gradient(180deg,#8a847b,#2e3138)"></div><div class="name">Dana Whitlock</div><div class="role">LAW OFFICE</div></div>
    <div class="attorney"><div class="portrait" role="img" aria-label="Portrait of attorney Leila Farrow in an office" style="background:linear-gradient(180deg,#a39d92,#3d3c3e)"></div><div class="name">Leila Farrow</div><div class="role">LAW OFFICE</div></div>
  </div>
</section>

<section class="practice" role="img" aria-label="Muted photo of business people shaking hands">
  <h2>PRACTICE AREAS</h2>
  <div class="practice-cols">
    <div class="col-left">
      <div class="col-head">AREAS OF PRACTICE</div>
      <div class="item">Employment Law <span class="star">★</span></div>
      <div class="item">Benefits/ERISA Law <span class="star">★</span></div>
      <div class="item">Civil Litigation <span class="star">★</span></div>
      <div class="item">Railway Labor Act <span class="star">★</span></div>
      <div class="item">Hotel Law <span class="star">★</span></div>
      <div class="item">Non-Profit Law <span class="star">★</span></div>
      <div class="item">Federal False Claims Act (Qui Tam) <span class="star">★</span></div>
      <div class="item">Human Resources <span class="star">★</span></div>
      <div class="item">Lectures and Training <span class="star">★</span></div>
    </div>
    <div class="col-right">
      <div class="col-head">INDUSTRIES</div>
      <div class="item"><span class="star">★</span> Construction</div>
      <div class="item"><span class="star">★</span> Manufacturing</div>
      <div class="item"><span class="star">★</span> Automotive</div>
      <div class="item"><span class="star">★</span> Retail</div>
      <div class="item"><span class="star">★</span> Non Profits and Religious Organizations</div>
      <div class="item"><span class="star">★</span> Financial and Banking Services</div>
      <div class="item"><span class="star">★</span> Computer Software Services</div>
      <div class="item"><span class="star">★</span> Engineering and Design</div>
      <div class="item"><span class="star">★</span> Hotel and Restaurant</div>
      <div class="item"><span class="star">★</span> Medical Practices</div>
    </div>
  </div>
</section>

<section class="chat">
  <div class="mark"></div>
  <p>NEED SOME LEGAL ASSISTANCE? LET'S HAVE A CHAT!</p>
</section>

<section class="evaluation">
  <h2>REQUEST A FREE CASE EVALUATION</h2>
  <div class="sub">Fill out the form below to receive a free and confidential initial consultation</div>
  <div class="field" style="left:268px">Full Name</div>
  <div class="field" style="left:437px">Phone</div>
  <div class="field" style="left:606px">Email</div>
  <div class="field" style="left:775px">Auto Accident</div>
  <div class="field message">Message</div>
  <div class="send">Send Request</div>
</section>

<section class="contact">
  <div class="icon"></div>
  <h2>CONTACT US</h2>
  <div class="contact-lines">
    <div><div class="label">PHONE</div><div class="value">(555) 014 - 2270</div></div>
    <div><div class="label">FACSIMLE:</div><div class="value">(555) 014 - 2285</div></div>
  </div>
  <div class="email-box">INFO@QUILLBROOKCOUNSEL.COM</div>
  <div class="address">QUILLBROOK &amp; ASSOCIATES, P.C. Two Harbor Plaza Suite 210 Eastport, NY 11900</div>
  <div class="social"><span></span><span></span><span></span><span></span></div>
</section>

<footer class="site-footer">
  <div class="copy">Copyright © 2015. All Rights Reserved. Quillbrook &amp; Associates, P.C.</div>
</footer>

</body>
</html>
```